Vantrel Web Services

This is a new It services company operating in Perth western Australia

we need a website that is easy to navigate without a cluttered feel to it it should have the following links and pages

About Us
Services
Clients
Contact Us
MY Vantrel (login for clients)

Hi it is a web based IT services company so we would expect customers to come to the website for 2 different purposes the first is to enquire about our services and then as they become customers come to our website to manage their services so whilst they are seperate we want do not want it to look like 2 different websites

hope this helps

Hi to update this we need a home page and templates for sub pages

this is a design brief only and not the coding of the pages or building of the site

```html
<!DOCTYPE html>
<html lang="en">
<head>
<meta charset="utf-8">
<title>Vantrel Web Services</title>
<link rel="stylesheet" href="https://fonts.googleapis.com/css2?family=Roboto+Condensed:wght@400;700&family=Arimo:wght@400;700&display=swap">
<style>
:root{
  --blue:#1d3fae;
  --navy:#0c2a96;
  --ink:#2e2e2e;
  --text:#6a6a6a;
  --rule:#e2e2e2;
  --dark:#353535;
  --footer:#343434;
  --white:#ffffff;
}
*{box-sizing:border-box;margin:0;padding:0}
html,body{width:692px;height:1200px;overflow:hidden;background:var(--white)}
body{position:relative;font-family:"Arimo",Arial,sans-serif;color:var(--text)}
.topline{position:absolute;left:0;top:0;width:692px;height:2px;background:var(--navy)}
.abs{position:absolute}
.cond{font-family:"Roboto Condensed",Arial,sans-serif}
h2{font-family:"Roboto Condensed",Arial,sans-serif;font-weight:400;color:var(--blue);font-size:11.5px}
p{font-size:6.6px;line-height:11.6px}

.brand{left:75px;top:22px;font-family:"Roboto Condensed",Arial,sans-serif;font-weight:400;font-size:16px;color:var(--blue)}
.nav a{position:absolute;top:27px;font-family:"Roboto Condensed",Arial,sans-serif;font-size:9.2px;color:var(--ink);text-decoration:none}
.nav .account{top:21px;left:541px;width:75px;height:22px;background:var(--navy);color:var(--white);display:flex;align-items:center;justify-content:center;border-radius:1px}

.hero{left:75px;top:61px;width:541px;height:271px;background:radial-gradient(ellipse at 55% 25%,#bfe3ee 0%,#5d9fbc 30%,#2a5f7c 60%,#1a3344 100%);overflow:hidden}
.hero-caption{position:absolute;left:0;bottom:0;width:100%;height:39px;background:rgba(20,20,20,.55);display:flex;align-items:center;padding-left:16px}
.hero-caption span{font-family:"Roboto Condensed",Arial,sans-serif;color:var(--white);font-size:11.4px}
.hero-arrows{position:absolute;right:17px;bottom:12px;display:flex;gap:6px}

.pager{display:flex;gap:7px}

.service{position:absolute;top:379px;width:128px}
.service .photo{width:128px;height:109px}
.service h3{margin-top:13px;font-family:"Roboto Condensed",Arial,sans-serif;font-weight:400;font-size:7.6px;color:var(--blue)}
.service p{margin-top:4px;font-size:6.2px;line-height:11.6px;color:#8a8a8a}
.btn{display:inline-flex;align-items:center;justify-content:center;height:21px;background:linear-gradient(#4a4a4a,#2a2a2a);color:var(--white);font-family:"Roboto Condensed",Arial,sans-serif;font-weight:400;font-size:7.8px;border-radius:1px}
.service .btn{position:absolute;top:191px;width:63px}

.ticks{list-style:none}
.ticks li{display:flex;align-items:center;height:15.7px;font-size:6.8px;color:var(--text)}
.ticks svg{margin-left:11px;margin-right:9px}

.feature{position:absolute;left:265px;width:165px;border-bottom:1px solid var(--rule);height:52px}
.feature h4{font-family:"Roboto Condensed",Arial,sans-serif;font-weight:400;font-size:7.6px;color:var(--blue);margin-bottom:3px}
.feature p{font-size:6.2px;line-height:11px}

.news{position:absolute;left:441px;width:176px;height:77px}
.news.ruled{border-bottom:1px solid var(--rule)}
.date{position:absolute;left:2px;top:0;width:29px;height:28px;background:var(--dark);color:var(--white);font-family:"Roboto Condensed",Arial,sans-serif;font-size:8px;text-align:center;line-height:12px;padding-top:2px}
.news h4{position:absolute;left:39px;top:0;width:138px;font-weight:400;font-size:6.7px;line-height:12px;color:var(--ink)}
.news p{position:absolute;left:1px;top:37px;font-size:6.2px;line-height:12px}

.divider{left:75px;width:541px;height:1px;background:var(--rule)}
.about{left:75px;top:893px;width:541px;text-align:center}
.about h2{font-size:13px}
.about p{margin:9px 20px 0;font-size:6.4px;line-height:17px}

.client{position:absolute;top:1040px;width:99px;height:46px;border:1px solid #ececec;display:flex;align-items:center;justify-content:center;gap:4px;font-size:10px;color:#9a9a9a}

.footer{left:0;top:1105px;width:692px;height:95px;background:var(--footer)}
.social{position:absolute;left:86px;top:22px;display:flex;gap:6px}
.social span{width:16px;height:16px;background:#6b6b6b;border-radius:2px}
.news-label{position:absolute;left:241px;top:22px;font-family:"Roboto Condensed",Arial,sans-serif;font-size:12px;color:#dcdcdc}
.news-copy{position:absolute;left:307px;top:22px;width:150px;padding-left:10px;border-left:1px solid #555;font-size:5.4px;line-height:11px;color:#cfcfcf}
.news-input{position:absolute;left:462px;top:22px;width:145px;height:23px;background:#efefef;display:flex;align-items:center;padding:0 8px;gap:6px;font-size:4.8px;color:#9a9a9a}
.news-input span{flex:1}
.footer-rule{position:absolute;left:86px;top:53px;width:520px;height:1px;background:#4c4c4c}
.copyright{position:absolute;left:0;top:72px;width:692px;text-align:center;font-size:5.8px;color:#cfcfcf}
</style>
</head>
<body>
<div class="topline"></div>

<header>
  <div class="abs brand">Vantrel</div>
  <nav class="nav">
    <a href="#" style="left:240px">Home</a>
    <a href="#" style="left:295px">About us</a>
    <a href="#" style="left:361px">Services</a>
    <a href="#" style="left:425px">Clients</a>
    <a href="#" style="left:483px">Contact us</a>
    <a href="#" class="account">MY Vantrel</a>
  </nav>
</header>

<section class="abs hero" role="img" aria-label="Team of business people standing in front of a large globe">
  <div class="hero-caption"><span>Neque porro quisquam est qui dolorem ipsum quia Sed ut perspiciatis unde omnis iste natus</span></div>
  <div class="hero-arrows">
    <svg width="14" height="14" viewBox="0 0 14 14"><circle cx="7" cy="7" r="7" fill="#ddd"/><path d="M8.3 4 5.3 7l3 3" fill="none" stroke="#333" stroke-width="1.6"/></svg>
    <svg width="14" height="14" viewBox="0 0 14 14"><circle cx="7" cy="7" r="7" fill="#ddd"/><path d="M5.7 4l3 3-3 3" fill="none" stroke="#333" stroke-width="1.6"/></svg>
  </div>
</section>

<section class="services">
  <h2 class="abs" style="left:75px;top:354px">Services</h2>
  <div class="abs pager" style="left:599px;top:356px">
    <svg width="5" height="8"><path d="M4 1 1 4l3 3" fill="none" stroke="#bbb"/></svg>
    <svg width="5" height="8"><path d="M1 1l3 3-3 3" fill="none" stroke="#bbb"/></svg>
  </div>
  <article class="service" style="left:75px">
    <div class="photo" role="img" aria-label="Business team in suits against a world map" style="background:linear-gradient(#5b6670,#1f2428)"></div>
    <h3>PREMIUM IT SOLUTIONS</h3>
    <p>Sui blanditiistes es prtiuptaum Deleniti-matququdolores etrste Molestiasexceuri sintsupaqui Sui blanditiistes es prtiuptatum cupaqui officiadeserunt.........</p>
    <span class="btn">READ MORE</span>
  </article>
  <article class="service" style="left:214px">
    <div class="photo" role="img" aria-label="Blue puzzle pieces labelled web development" style="background:radial-gradient(circle at 55% 50%,#4fa0ff,#0b2f9c 70%,#061a5a)"></div>
    <h3>WEB DEVELOPMENT</h3>
    <p>Sui blanditiistes es prtiuptaum Deleniti-matququdolores etrste Molestiasexceuri sintsupaqui Sui blanditiistes es prtiuptatum cupaqui officiadeserunt.........</p>
    <span class="btn">READ MORE</span>
  </article>
  <article class="service" style="left:351px">
    <div class="photo" role="img" aria-label="Hand touching a network of icons on a map" style="background:linear-gradient(135deg,#e4eef4,#8eaec2 60%,#6d8899)"></div>
    <h3>DATABASE MANAGEMENT</h3>
    <p>Sui blanditiistes es prtiuptaum Deleniti-matququdolores etrste Molestiasexceuri sintsupaqui Sui blanditiistes es prtiuptatum cupaqui officiadeserunt.........</p>
    <span class="btn">READ MORE</span>
  </article>
  <article class="service" style="left:489px">
    <div class="photo" role="img" aria-label="Hand on a computer mouse with data charts" style="background:linear-gradient(160deg,#3f8fa8,#a9dbe6 55%,#f2f6f8)"></div>
    <h3>TECHNICALSUPPORT</h3>
    <p>Sui blanditiistes es prtiuptaum Deleniti-matququdolores etrste Molestiasexceuri sintsupaqui Sui blanditiistes es prtiuptatum cupaqui officiadeserunt.........</p>
    <span class="btn">READ MORE</span>
  </article>
</section>

<section class="what-we-do">
  <h2 class="abs" style="left:75px;top:626px">What We Do</h2>
  <p class="abs" style="left:75px;top:648px;width:170px">Sed ut perspiciatis unde omnis iste natus error sit volup-tatem accusantium doloremque laudantium, totam rem aperiam laudantium, totam rem ...</p>
  <h3 class="abs cond" style="left:75px;top:706px;font-weight:400;font-size:8.3px;color:var(--blue)">Neque porro quisquam est qui dolorem</h3>
  <ul class="abs ticks" style="left:75px;top:727px">
    <li><svg width="7" height="7" viewBox="0 0 7 7"><path d="M.5 3.5 2.6 6 6.5.5" fill="none" stroke="#1d3fae" stroke-width="1"/></svg>The Application Process</li>
    <li><svg width="7" height="7" viewBox="0 0 7 7"><path d="M.5 3.5 2.6 6 6.5.5" fill="none" stroke="#1d3fae" stroke-width="1"/></svg>Tuition &amp; Fees</li>
    <li><svg width="7" height="7" viewBox="0 0 7 7"><path d="M.5 3.5 2.6 6 6.5.5" fill="none" stroke="#1d3fae" stroke-width="1"/></svg>International Cadets</li>
    <li><svg width="7" height="7" viewBox="0 0 7 7"><path d="M.5 3.5 2.6 6 6.5.5" fill="none" stroke="#1d3fae" stroke-width="1"/></svg>Summer Programs</li>
    <li><svg width="7" height="7" viewBox="0 0 7 7"><path d="M.5 3.5 2.6 6 6.5.5" fill="none" stroke="#1d3fae" stroke-width="1"/></svg>Registration</li>
    <li><svg width="7" height="7" viewBox="0 0 7 7"><path d="M.5 3.5 2.6 6 6.5.5" fill="none" stroke="#1d3fae" stroke-width="1"/></svg>Registration Forms</li>
  </ul>
  <span class="abs btn" style="left:75px;top:838px;width:110px">CLICK HERE FOR MORE INFO</span>
</section>

<section class="featured">
  <h2 class="abs" style="left:265px;top:626px">Featured Services</h2>
  <div class="feature" style="top:651px"><h4>Sed ut perspiciatis unde omnis iste natus</h4><p>Neque porro quisquam est, qui dolorem ipsum quia dolor consectetur, adipisci velit, sed quia non numquam.....</p></div>
  <div class="feature" style="top:703px"><h4>Sed ut perspiciatis unde omnis iste natus</h4><p>Neque porro quisquam est, qui dolorem ipsum quia dolor consectetur, adipisci velit, sed quia non numquam.....</p></div>
  <div class="feature" style="top:756px"><h4>Sed ut perspiciatis unde omnis iste natus</h4><p>Neque porro quisquam est, qui dolorem ipsum quia dolor consectetur, adipisci velit, sed quia non numquam.....</p></div>
  <div class="feature" style="top:808px;border-bottom:0"><h4>Sed ut perspiciatis unde omnis iste natus</h4><p>Neque porro quisquam est, qui dolorem ipsum quia dolor consectetur, adipisci velit, sed quia non numquam.....</p></div>
</section>

<section class="latest-news">
  <h2 class="abs" style="left:441px;top:626px">Latest News</h2>
  <article class="news ruled" style="top:653px"><div class="date">MAY<br>30</div><h4>Neque porro quisquam est qui dolorem ipsum quia dolor sit amet,</h4><p>Sed ut perspiciatis unde omnis iste natus error sit voluuarchi-tecto beatae vitae dicta sunt explicabo....</p></article>
  <article class="news ruled" style="top:730px"><div class="date">MAY<br>30</div><h4>Neque porro quisquam est qui dolorem ipsum quia dolor sit amet,</h4><p>Sed ut perspiciatis unde omnis iste natus error sit voluuarchi-tecto beatae vitae dicta sunt explicabo....</p></article>
  <article class="news" style="top:808px"><div class="date">MAY<br>30</div><h4>Neque porro quisquam est qui dolorem ipsum quia dolor sit amet,</h4><p>Sed ut perspiciatis unde omnis iste natus error sit voluuarchi-tecto beatae vitae dicta sunt explicabo....</p></article>
</section>

<div class="abs divider" style="top:882px"></div>

<section class="abs about">
  <h2>About Vantrel</h2>
  <p>Sed ut perspiciatis unde omnis iste natus error sit voluptatem accusantium doloremque laudantium, totam rem aperiam, eaque ipsa quae ab illo inventore veritatis et quasi architecto beatae vitae dicta sunt explicabo. Nemo enim ipsam voluptatem quia voluptas sit aspernatur aut odit aut fugit, sed quia consequuntur magni dolores numquam eius modi tempora incidunt ut labore et dolore magnam aliquam quaerat voluptatem.</p>
  <span class="btn" style="width:110px;margin-top:14px">CLICK HERE FOR MORE INFO</span>
</section>

<section class="clients">
  <h2 class="abs" style="left:77px;top:1015px;font-size:12px">Clients</h2>
  <div class="abs pager" style="left:603px;top:1019px">
    <svg width="5" height="8"><path d="M4 1 1 4l3 3" fill="none" stroke="#bbb"/></svg>
    <svg width="5" height="8"><path d="M1 1l3 3-3 3" fill="none" stroke="#bbb"/></svg>
  </div>
  <div class="client" style="left:78px">Northgate</div>
  <div class="client" style="left:188px">Keplon</div>
  <div class="client" style="left:298px">Ardena</div>
  <div class="client" style="left:407px">Tessro</div>
  <div class="client" style="left:514px">Holvik</div>
</section>

<footer class="abs footer">
  <div class="social"><span></span><span></span><span></span><span></span><span></span></div>
  <div class="news-label">NewsLetter :</div>
  <div class="news-copy">In venenatis neque a eros laoreet eu placerat erat suscipit. Fusce cursus, erat ut scelerisque condimentum</div>
  <div class="news-input">
    <svg width="10" height="7" viewBox="0 0 10 7"><rect x=".5" y=".5" width="9" height="6" fill="none" stroke="#aaa"/><path d="M.5.5 5 4 9.5.5" fill="none" stroke="#aaa"/></svg>
    <span>Enter Your Email Address :</span>
    <svg width="5" height="8"><path d="M1 1l3 3-3 3" fill="none" stroke="#999"/></svg>
  </div>
  <div class="footer-rule"></div>
  <div class="copyright">Copy Right 2014 VANTREL All Right REseved.</div>
</footer>
</body>
</html>
```